FULL Page Ad - Modern Elegant

- I need a 8.5" x 11" trim ad with 0.25" bleed. Live information should be at least 0.5" from edges.

Target Market(s)

Insurance Company Decision Makers

Industry/Entity Type

Insurance

Colors

Designer to choose colors to be used in the design.

Requirements
Nice to have
• Would like colors matched to our logo. Would like incorporation of natural disasters (tornado, hail, hurricane or things like house fires)

```html
<!DOCTYPE html>
<html lang="en">
<head>
<meta charset="utf-8">
<title>Beacon Adjusters – Emergency Response Center Ad</title>
<link rel="stylesheet" href="https://fonts.googleapis.com/css2?family=Oswald:wght@500;700&family=Roboto+Condensed:wght@400;700&display=swap">
<style>
  :root{
    --page-bg:#ecebe8;
    --white:#ffffff;
    --orange:#d9782a;
    --purple:#3a22a8;
    --navy:#1c1f5e;
  }
  *{margin:0;padding:0;box-sizing:border-box}
  html,body{width:1200px;height:949px;overflow:hidden;background:var(--page-bg)}
  .ad{
    position:absolute;left:260px;top:34px;width:680px;height:880px;
    overflow:hidden;background:var(--navy);
    font-family:"Roboto Condensed",sans-serif;
    box-shadow:0 6px 24px rgba(0,0,0,.18);
  }
  .storm-backdrop{
    position:absolute;inset:0;
    background:
      radial-gradient(ellipse 55% 30% at 62% 56%, rgba(214,70,60,.85), transparent 70%),
      radial-gradient(ellipse 70% 40% at 45% 66%, rgba(150,40,80,.7), transparent 75%),
      linear-gradient(180deg,#2f3fa8 0%,#3a2f9a 30%,#4a2a80 52%,#6a2450 68%,#2a1a4a 100%);
  }
  .brand-tab{
    position:absolute;left:0;top:0;width:450px;height:170px;
    background:var(--white);border-bottom-right-radius:80px;
    display:flex;align-items:center;padding-left:50px;
  }
  .brand-name{
    display:flex;align-items:center;gap:14px;
    font-family:"Roboto Condensed",sans-serif;font-weight:700;font-size:38px;
    color:var(--purple);line-height:1;white-space:nowrap;
  }
  .brand-dot{width:22px;height:22px;border-radius:50%;background:var(--orange);flex:none}
  .service-badge{
    position:absolute;left:150px;top:170px;width:140px;height:82px;
    background:var(--orange);border-radius:0 0 22px 22px;
    color:var(--white);text-align:center;font-family:"Oswald",sans-serif;
    padding-top:6px;
  }
  .service-badge .hours{font-size:40px;font-weight:700;line-height:1}
  .service-badge .label{font-size:18px;font-weight:500;letter-spacing:2px}
  .headline{
    position:absolute;left:44px;top:290px;
    font-family:"Oswald",sans-serif;font-weight:700;font-size:74px;
    line-height:1.02;color:var(--white);text-transform:uppercase;
    text-shadow:0 3px 8px rgba(0,0,0,.35);
  }
  .contact-shape{position:absolute;left:0;top:0;width:680px;height:880px}
  .portrait{
    position:absolute;left:70px;top:560px;width:380px;height:320px;
    background:linear-gradient(180deg,#5a4a78 0%,#8a86a8 55%,#b9b6c9 100%);
  }
  .company-block{
    position:absolute;left:420px;top:500px;width:250px;color:var(--white);
  }
  .company-name{font-family:"Oswald",sans-serif;font-weight:700;font-size:28px;line-height:1.05}
  .company-legal{font-size:14px;font-weight:700;letter-spacing:.3px;margin-top:2px}
  .company-phone{display:flex;align-items:center;gap:8px;font-family:"Oswald",sans-serif;font-weight:700;font-size:34px;margin-top:4px}
  .company-phone svg{width:24px;height:24px}
  .contact-list{position:absolute;left:500px;top:660px;width:170px;color:var(--white);font-size:17px;line-height:1.3}
  .contact-item{display:flex;flex-direction:column;align-items:center;text-align:center;margin-bottom:22px}
  .contact-item svg{width:26px;height:26px;margin-bottom:6px}
  .contact-email{font-size:15px;font-weight:700}
</style>
</head>
<body>
<main class="ad">
  <div class="storm-backdrop" role="img" aria-label="Dramatic stormy sky with a tornado funnel and red glow on the horizon"></div>

  <header class="brand-tab">
    <div class="brand-name"><span class="brand-dot"></span><span>BEACON ADJUSTERS</span></div>
  </header>

  <div class="service-badge">
    <div class="hours">24/7</div>
    <div class="label">SERVICE</div>
  </div>

  <h1 class="headline">Emergency<br>Response<br>Center</h1>

  <div class="portrait" role="img" aria-label="Portrait of a seated claims adjuster in a light shirt"></div>

  <svg class="contact-shape" viewBox="0 0 680 880" aria-hidden="true">
    <path d="M390 880 C 470 780 470 640 430 600 L 680 600 L 680 880 Z" fill="var(--purple)"/>
    <path d="M420 880 C 495 780 495 650 460 610 L 680 610 L 680 880 Z" fill="var(--orange)"/>
    <path d="M470 475 L 680 475 L 680 640 L 470 640 A 82 82 0 0 1 470 475 Z" fill="var(--purple)"/>
  </svg>

  <section class="company-block">
    <div class="company-name">BEACON ADJUSTERS</div>
    <div class="company-legal">HUDSON RIDGE CLAIM SERVICES, INC.</div>
    <div class="company-phone">(800) 555-0148
      <svg viewBox="0 0 24 24" fill="none" stroke="#fff" stroke-width="2"><path d="M5 3h4l2 5-3 2a12 12 0 0 0 6 6l2-3 5 2v4a2 2 0 0 1-2 2A17 17 0 0 1 3 5a2 2 0 0 1 2-2z"/></svg>
    </div>
  </section>

  <section class="contact-list">
    <div class="contact-item">
      <svg viewBox="0 0 24 24" fill="none" stroke="#fff" stroke-width="2"><path d="M12 22s7-7 7-12a7 7 0 0 0-14 0c0 5 7 12 7 12z"/><circle cx="12" cy="10" r="2.5"/></svg>
      <span>412 Mill Lane<br>PO Box 218<br>Cedar Falls, NY 12000</span>
    </div>
    <div class="contact-item">
      <svg viewBox="0 0 24 24" fill="none" stroke="#fff" stroke-width="2"><rect x="3" y="5" width="18" height="14" rx="1"/><path d="M3 6l9 7 9-7"/></svg>
      <span class="contact-email">info@beaconadjusters.com</span>
    </div>
  </section>
</main>
</body>
</html>
```